TR Ventura Website (professional site for investors and funds)

We want to make a website for an Holding Company that owns other companies' shares in different fields. TR is the name of the holding.
We still do not have a logo or preferred colors for the company. The company, through this website, will send a clear message: it's not important where we are, it's important what we do but more than that why we do what we do.
We search for inspiration in a simple layout because we want that the user feels comfortable and guided while exploring it. The content of the website aspire to be very impressive through one or more background images.

Below, the structure of the pages explained shortly.
To learn more, we have attached a draft of the website.

Home: page with a huge backround image that fill the whole page (maybe is better to merge the navbar with the image top color?).
About: with the same huge background image, we explain which are our fields.
Why: with the same huge background image, we explain which is our why.
Projects: dropdown list with project 1, project 2, project 3. If clicked, a box like about/why pops up in order to explain projects in detail.

Target Market(s)

Investors, Entrepreneurs

Industry/Entity Type

It Company

Number of Pages Required

4 page

Font styles to use
Sans Serif

Requirements
Must have
• An idea for the background image (color and design)
• Menu
• Page layout for about/why/projects
Nice to have
• Tips for color to use in this design
Should not have
• Complicated stuff

```html
<!DOCTYPE html>
<html lang="en">
<head>
<meta charset="utf-8">
<title>TR Ventura</title>
<link href="https://fonts.googleapis.com/css2?family=Open+Sans:wght@300;400;600;700&display=swap" rel="stylesheet">
<style>
:root{
  --brand:#2f8fe0;
  --brand-dark:#1f6fc0;
  --ink:#1d1d1d;
  --muted:#555;
  --white:#ffffff;
  --panel:rgba(255,255,255,0.96);
  --glass:rgba(225,236,250,0.78);
  --nav-bg:rgba(255,255,255,0.97);
  --footer-bg:#f4f5f7;
}
*{box-sizing:border-box;margin:0;padding:0}
html,body{width:1200px;height:2799px;overflow:hidden}
body{position:relative;font-family:"Open Sans",Arial,sans-serif;color:var(--ink);background:var(--white)}
.abs{position:absolute}

/* Navigation */
.site-nav{position:absolute;left:0;top:0;width:1200px;height:56px;background:var(--nav-bg);z-index:5}
.brand{position:absolute;left:246px;top:10px;font-size:30px;font-weight:700;color:var(--brand);line-height:36px;letter-spacing:1px}
.menu{position:absolute;top:18px;left:757px;display:flex;gap:14px;font-size:12px;align-items:center}
.menu a{color:var(--ink);text-decoration:none;line-height:20px}
.menu .active{background:#6fa6d8;color:var(--white);padding:0 12px;border-radius:10px;font-weight:600}
.menu .current{color:var(--brand-dark)}
.dropdown{position:absolute;left:882px;top:45px;width:94px;height:86px;background:#cfe3f7;border-radius:4px;padding:10px 12px;font-size:9.5px;line-height:22px;z-index:6;box-shadow:0 2px 6px rgba(0,0,0,.15)}
.dropdown span{display:block;color:#234}

/* Sections */
.band{position:absolute;left:0;width:1200px}
.hero{top:56px;height:631px;background:linear-gradient(180deg,#7f9bc0 0%,#506d95 30%,#2b3a57 58%,#1a1f25 82%,#2a2418 100%)}
.about{top:687px;height:685px;background:radial-gradient(ellipse at 45% 70%,#8a6a4d 0%,#3d3226 35%,#141414 75%),#111}
.why{top:1372px;height:685px;background:linear-gradient(180deg,#1d4fb6 0%,#3d7be0 35%,#6b9fe2 55%,#c9d7ea 72%,#3c4a62 88%,#1a2436 100%)}
.projects{top:2057px;height:686px;background:linear-gradient(180deg,#3b78cc 0%,#7fa9dc 40%,#b9d0ea 62%,#9db5cf 82%,#3b5b3a 94%,#1f3a22 100%)}

.hero-title{position:absolute;left:0;width:1200px;top:140px;text-align:center;color:var(--white);font-size:34px;font-weight:300}
.hero-sub{position:absolute;left:380px;width:440px;top:186px;text-align:center;color:var(--white);font-size:13px;line-height:24px}
.cta{position:absolute;left:540px;top:252px;width:120px;height:34px;border-radius:17px;background:var(--brand-dark);color:var(--white);font-size:8px;font-weight:700;letter-spacing:.5px;text-align:center;line-height:34px}
.scroll-down{position:absolute;left:568px;width:64px;height:64px;border-radius:50%;background:rgba(30,30,30,.55)}
.scroll-down svg{position:absolute;left:20px;top:24px}

.eyebrow{position:absolute;left:0;width:1200px;text-align:center;color:rgba(255,255,255,.85);font-size:7px;letter-spacing:1px;font-weight:600}
.section-title{position:absolute;left:0;width:1200px;text-align:center;color:var(--white);font-size:27px;font-weight:400}
.section-title.dark{color:var(--ink)}
.eyebrow.dark{color:#444}
.rule{position:absolute;left:588px;width:24px;height:3px;background:var(--white)}
.rule.dark{background:var(--ink)}

.field-card{position:absolute;top:832px;width:222px;height:178px;background:var(--panel);border-radius:4px;padding:18px 22px}
.field-card h3{display:flex;align-items:center;gap:8px;color:var(--brand);font-size:18px;font-weight:400;margin-bottom:10px}
.field-card p{font-size:9.5px;line-height:14px;color:var(--ink)}
.field-card .more{display:block;margin-top:14px;font-size:8.5px;color:var(--brand-dark)}

.glass-box{position:absolute;left:248px;width:702px;background:var(--glass);border-radius:5px}
.why-box{top:1532px;height:220px;display:flex}
.why-box .col{width:50%;padding:18px 20px;font-size:10px;line-height:15px}
.why-box .col+.col{border-left:1px solid rgba(80,110,160,.35)}
.why-box p{margin-bottom:8px}
.why-box ul{list-style:none;color:var(--brand-dark);margin-bottom:8px}
.why-box li::before{content:"› "}

.project-box{top:2219px;height:278px;padding:22px 24px}
.project-head{text-align:center;font-size:19px;font-weight:400;margin-bottom:20px}
.project-head svg{display:block;margin:0 auto 6px}
.project-cols{display:flex;gap:26px;font-size:9.5px;line-height:14.5px}
.project-cols div{width:50%}
.project-cols p{margin-bottom:8px}
.slide-arrow{position:absolute;top:2344px}

.site-footer{position:absolute;left:0;top:2743px;width:1200px;height:56px;background:var(--footer-bg)}
.copyright{position:absolute;left:248px;top:21px;font-size:8px;font-weight:600;color:var(--ink)}
.copyright span{color:var(--brand)}
.social{position:absolute;left:800px;top:18px;display:flex;gap:11px}
.social i{display:block;width:18px;height:18px;border-radius:50%;border:1.5px solid #d9534f}
.social i:nth-child(-n+3){border-color:#3b8bd6}
</style>
</head>
<body>

<header class="site-nav">
  <div class="brand">TR</div>
  <nav class="menu">
    <a class="active">Home</a><a>About</a><a>Why</a><a class="current">Projects</a>
  </nav>
  <div class="dropdown"><span>Wind Energy</span><span>I.T.</span><span>Consulting</span></div>
</header>

<section class="band hero" role="img" aria-label="Night city skyline seen from a hillside, lit towers by a harbour">
  <h1 class="hero-title">Welcome to TR Ventura</h1>
  <p class="hero-sub">It's not important where we are, it's important what we do but more than that why we do what we do.</p>
  <div class="cta">LET'S GET STARTED</div>
  <div class="scroll-down" style="top:522px"><svg width="24" height="14" viewBox="0 0 24 14"><path d="M1 1l11 11L23 1" fill="none" stroke="#fff" stroke-width="1.5"/></svg></div>
</section>

<section class="band about" role="img" aria-label="Hands typing on a laptop, wristwatch, pen on a wooden desk">
  <div class="scroll-down" style="top:576px"><svg width="24" height="14" viewBox="0 0 24 14"><path d="M1 1l11 11L23 1" fill="none" stroke="#fff" stroke-width="1.5"/></svg></div>
</section>
<div class="eyebrow" style="top:757px">LEARN MORE ABOUT US</div>
<h2 class="section-title" style="top:762px">About Us</h2>
<div class="rule" style="top:809px"></div>

<article class="field-card" style="left:248px">
  <h3><svg width="18" height="18" viewBox="0 0 18 18"><g stroke="#2f8fe0" stroke-width="1.6" fill="none"><path d="M9 8v9"/><path d="M9 8L4 2"/><path d="M9 8l7-1"/><path d="M9 8L5 13"/></g></svg>Wind Energy</h3>
  <p>Lorem ipsum dolor sit amet, consectetur adipiscing elit. Nullam blandit tellus eu eros scelerisque, quis finibus sem efficitur. Proin tempus, est ut accumsan suscipit, sem lorem dictum odio.</p>
  <span class="more">Keep Reading ›</span>
</article>
<article class="field-card" style="left:489px">
  <h3><svg width="20" height="16" viewBox="0 0 20 16"><g stroke="#2f8fe0" stroke-width="1.4" fill="none"><rect x="1" y="2" width="12" height="9"/><path d="M4 14h6"/><rect x="15" y="1" width="4" height="14"/></g></svg>IT</h3>
  <p>Lorem ipsum dolor sit amet, consectetur adipiscing elit. Nullam blandit tellus eu eros scelerisque, quis finibus sem efficitur. Proin tempus, est ut accumsan suscipit, sem lorem dictum odio.</p>
  <span class="more">Keep Reading ›</span>
</article>
<article class="field-card" style="left:730px">
  <h3><svg width="22" height="18" viewBox="0 0 22 18"><rect x="1" y="1" width="11" height="8" rx="2" fill="#2f8fe0"/><rect x="9" y="7" width="12" height="9" rx="2" fill="#6fb2ee"/></svg>Consulting</h3>
  <p>Lorem ipsum dolor sit amet, consectetur adipiscing elit. Nullam blandit tellus eu eros scelerisque, quis finibus sem efficitur. Proin tempus, est ut accumsan suscipit, sem lorem dictum odio.</p>
  <span class="more">Keep Reading ›</span>
</article>

<section class="band why" role="img" aria-label="Snow-covered mountain ridge under a deep blue cloudy sky">
  <div class="scroll-down" style="top:546px"><svg width="24" height="14" viewBox="0 0 24 14"><path d="M1 1l11 11L23 1" fill="none" stroke="#fff" stroke-width="1.5"/></svg></div>
</section>
<div class="eyebrow" style="top:1440px">WE'RE SIMPLE · WE SUPPORT</div>
<h2 class="section-title" style="top:1449px">Why Us</h2>
<div class="rule" style="top:1496px"></div>

<div class="glass-box why-box">
  <div class="col">
    <p>Lorem ipsum dolor sit amet, consectetur adipiscing elit. Nullam blandit tellus eu eros scelerisque, quis finibus sem efficitur. Proin tempus, est ut accumsan suscipit, sem lorem dictum odio, at consequat ligula velit nec mauris.</p>
    <p>Aliquam eget consequat lectus. Nullam augue erat, congue nec diam vitae, vehicula feugiat enim. Sed accumsan nulla pellentesque, facilisis odio nec, vestibulum mi.</p>
    <p>Nam sed purus tempor, maximus libero ac, porttitor lectus. Proin auctor commodo orci ac tincidunt. Aliquam nec libero vitae ipsum dignissim pellentesque sit amet a est ultrices nec.</p>
  </div>
  <div class="col">
    <p>Integer ultrices nec mauris vel faucibus. Mauris at nisi laoreet, iaculis ex non, laoreet orci. Pellentesque nec sodales nisl. Nunc id est in nisi ullamcorper convallis in a justo. Lorem ipsum dolor sit amet, consectetur adipiscing elit.</p>
    <ul>
      <li>Cras sodales pharetra mi, nec finibus orci dignissim pellentesque.</li>
      <li>Nam lorem nunc, vulputate vitae porta vel, facilisis vitae quam.</li>
      <li>Donec semper tincidunt dolor, ac sagittis sem maximus vel.</li>
      <li>Ut facilisis elementum arcu a elementum.</li>
      <li>Ut vitae elementum dui.</li>
    </ul>
    <p>Donec scelerisque nulla sit amet dolor iaculis, lacinia auctor sapien convallis. Maecenas vel elit libero.</p>
  </div>
</div>

<section class="band projects" role="img" aria-label="Wind turbines on green fields under a pale blue cloudy sky"></section>
<div class="eyebrow dark" style="top:2125px">WHAT WE CAN DO FOR YOU</div>
<h2 class="section-title dark" style="top:2135px">Our Projects</h2>
<div class="rule dark" style="top:2179px"></div>

<svg class="slide-arrow" style="left:152px" width="14" height="26" viewBox="0 0 14 26"><path d="M12 1L2 13l10 12" fill="none" stroke="#fff" stroke-width="1.5"/></svg>
<svg class="slide-arrow" style="left:1034px" width="14" height="26" viewBox="0 0 14 26"><path d="M2 1l10 12L2 25" fill="none" stroke="#fff" stroke-width="1.5"/></svg>

<div class="glass-box project-box" style="background:rgba(236,242,250,0.85)">
  <h3 class="project-head"><svg width="22" height="26" viewBox="0 0 22 26"><g stroke="#1d1d1d" stroke-width="1.8" fill="none"><path d="M11 11v14"/><path d="M11 11L6 2"/><path d="M11 11l10 1"/><path d="M11 11L3 17"/></g></svg>Wind Energy</h3>
  <div class="project-cols">
    <div>
      <p>Lorem ipsum dolor sit amet, consectetur adipiscing elit. Nullam blandit tellus eu eros scelerisque, quis finibus sem efficitur. Proin tempus, est ut accumsan suscipit, sem lorem dictum odio, at consequat ligula velit nec mauris.</p>
      <p>Aliquam eget consequat lectus. Nullam augue erat, congue nec diam vitae, vehicula feugiat enim. Sed accumsan nulla pellentesque, facilisis odio nec, vestibulum mi.</p>
      <p>Nam sed purus tempor, maximus libero ac, porttitor lectus. Proin auctor commodo orci ac tincidunt. Aliquam nec libero vitae ipsum dignissim pellentesque sit amet a est.</p>
    </div>
    <div>
      <p>Integer ultrices nec mauris vel faucibus. Mauris at nisi laoreet, iaculis ex non, laoreet orci. Pellentesque nec sodales nisl. Nunc id est in nisi ullamcorper convallis in a justo. Lorem ipsum dolor sit amet, consectetur adipiscing elit.</p>
      <p>Integer ultrices nec mauris vel faucibus. Mauris at nisi laoreet, iaculis ex non, laoreet orci. Pellentesque nec sodales nisl. Nunc id est in nisi ullamcorper convallis in a justo. Lorem ipsum dolor sit amet, consectetur adipiscing elit.</p>
      <p>Donec scelerisque nulla sit amet dolor iaculis, lacinia auctor sapien convallis. Maecenas vel elit libero.</p>
    </div>
  </div>
</div>

<footer class="site-footer">
  <div class="copyright">Copyright © 2017 - <span>TR Ventura</span> - All Rights Reserved</div>
  <div class="social" aria-label="Social links"><i></i><i></i><i></i><i></i><i></i><i></i></div>
</footer>

</body>
</html>
```